energy rating company

Web Design graphics and layout only

To create two pages for the website. First the home page and the second is the design for the job board for our clients use after login. I have attached files that explain in detail what the pages should have and the purpose/desires of each object. Please read these thoroughly.

The webpages need to be clean, professional, easy on the eye, obvious in all its buttons and functions with a strong call to action on the home page and branding and clean, great and obvious looking buttons and very simple but dynamic as well. We wish to be seen as contemporary.

Business Concept

Our business concept is simple, to build a website whereby our clients will be able to upload jobs for energy raters to quote on and subsequent complete the work if their quote is selected. To link energy ratings that are required with energy raters via our website. Similarly to the varlo website, jobs will be “advertised” on the job board and raters will select which jobs they wish to quote for.

I have attached a Word document explaining all the parts of the website and another word document showing what we are sort of after and a excel spreadsheet as well. Please read these in conjunction with this brief!
Updates

Dear All

I have submitted with my brief a word doc and excel spreadsheet of the two pages I want created.  However this is not the layout or design I want, I only put it together so that you will need to know what is required on each page.  Feel free to change and redesign it all.

Also the second page does not require the "process" logo or any other menu items except the first five being Home, How it works, About Us, testimonials and Contact us as per the home page.

We also are looking for something very professional and very clean.  It should be very easy to see exactly what you are looking for.

I will also extend the deadline for new designers!!  I am excited to see your talents!!

Thanks

I have increase budget and posted a note saying feel free to change all the details layout etc on my brief just include everything!!! 

Wanting a professional corporate look...

Want a professional corporate look

We have changed our minds and you we no longer require the process to be on the home page.

Thanks

Target Market(s)

Target Market

Home Inspection Companies
Pest Inspection Companies
Residential home buyers/sellers
Real Estate companies

Industry/Entity Type

It Company

Number of Pages Required

1 page

Requirements
Must have
• Colours and Styles

• The website should be mainly white as I believe it is seen as clean and simple with colour from the logos, but can be swayed if it projects the image we are after.

• It should be obvious and process orientated and I do believe symbols, pictures, etc should replace words where possible.

```html
<!DOCTYPE html>
<html lang="en">
<head>
<meta charset="utf-8">
<title>Voltaro Australia – Home and Job Board</title>
<link rel="stylesheet" href="https://fonts.googleapis.com/css2?family=Arimo:wght@400;700&family=PT+Sans:wght@400;700&family=Noto+Serif:ital@0;1&display=swap">
<style>
:root{
  --bg-green-top:#5fb132;
  --bg-green:#2f9a3c;
  --nav-green:#1e7a44;
  --brand-green:#4aa32a;
  --text-green:#3aa520;
  --teal:#1d9a6a;
  --orange-1:#f2b23a;
  --orange-2:#d97f12;
  --brand-orange:#c8651a;
  --text-grey:#4a4a4a;
  --soft-grey:#8a8a8a;
  --panel-grey:#f1f1f1;
  --row-grey:#ececec;
  --head-mint:#e3f5ec;
  --lime:#9dc236;
  --red:#d0231c;
}
*{box-sizing:border-box;margin:0;padding:0}
html,body{width:1200px;height:2180px;overflow:hidden}
body{position:relative;font-family:"Arimo",Arial,sans-serif;color:var(--text-grey);
  background:linear-gradient(180deg,var(--bg-green-top) 0,var(--bg-green) 560px,var(--bg-green) 1150px,#6bb535 1167px,var(--bg-green-top) 1170px,var(--bg-green) 1700px,#2a9440 2180px)}
.abs{position:absolute}
.sheet{position:absolute;left:74px;width:1055px;background:#fff;border-radius:8px;box-shadow:0 2px 6px rgba(0,0,0,.2)}
.copyright{position:absolute;left:74px;font-size:12px;color:#a9e58f}
.logo-box{position:absolute;left:69px;width:363px;height:137px;background:linear-gradient(#fff,#f0f0f0);border-radius:6px;box-shadow:0 2px 5px rgba(0,0,0,.25);display:flex;align-items:center;gap:16px;padding-left:28px}
.logo-dot{width:96px;height:96px;border-radius:50%;background:#f0a820}
.logo-name{font-family:"PT Sans",sans-serif;font-weight:700;font-size:52px;line-height:1;color:var(--brand-orange)}
.logo-name small{display:block;font-size:22px;letter-spacing:3px}
.main-nav{position:absolute;left:451px;top:30px;width:656px;height:54px;background:var(--nav-green);border-radius:0 0 8px 8px;display:flex;align-items:center;justify-content:space-around;font-family:"PT Sans",sans-serif;font-size:18px;color:#fff}
.cta{position:absolute;top:104px;width:205px;height:69px;border-radius:8px;background:linear-gradient(var(--orange-1),var(--orange-2));color:#fff;font-family:"PT Sans",sans-serif;font-size:24px;text-align:center;display:flex;flex-direction:column;justify-content:center;line-height:1.05;box-shadow:0 2px 3px rgba(0,0,0,.25)}
.cta small{font-size:15px}
.process{position:absolute;left:95px;top:204px;width:1009px;height:141px;border-radius:10px;background:linear-gradient(#f7f7f7,#fff 50%,#efefef);display:flex;align-items:center;justify-content:space-around;padding:0 40px;font-family:"PT Sans",sans-serif;font-size:21px;color:#333;text-align:center}
.process .step{width:130px;line-height:1.05}
.intro{position:absolute;left:104px;top:366px;width:650px;font-weight:700;font-size:19px;line-height:26px;color:var(--text-green)}
.lead{position:absolute;left:104px;top:463px;width:650px;font-size:16px;line-height:22px;color:#333}
.callout{position:absolute;left:71px;top:528px;width:701px;height:157px;border-radius:8px;background:linear-gradient(#fff,#fde9c0);box-shadow:0 1px 4px rgba(0,0,0,.2);padding:20px 33px;color:#e39a12;font-size:22px;line-height:32px}
.callout .big{font-size:27px;margin-top:16px}
.register{position:absolute;left:104px;top:700px;width:660px;font-weight:700;font-size:16px;line-height:22px;color:#8a8a8a}
.benefits{position:absolute;left:118px;top:781px;list-style:none;font-size:16px;line-height:22px;color:#333}
.benefits li{display:flex;align-items:center;gap:8px}
.free-note{position:absolute;left:104px;top:954px;width:640px;font-weight:700;font-size:16px;line-height:22px;color:#111}
.login{position:absolute;left:791px;top:368px;width:340px;height:201px;border-radius:6px;background:linear-gradient(#6fac35,#a2c53a);padding:10px 22px;color:#fff}
.login label{display:flex;align-items:center;gap:8px;font-family:"PT Sans",sans-serif;font-size:21px;color:#111}
.field{height:36px;background:#fff;border-radius:6px;margin:6px 0 12px;padding:0 12px;line-height:36px;font-size:17px;color:#777;box-shadow:inset 0 1px 3px rgba(0,0,0,.3)}
.login .forgot{font-size:13px}
.bullet{width:10px;height:10px;border-radius:50%;background:var(--brand-green);box-shadow:0 0 0 2px #2c6c1c inset}
.testimonials{position:absolute;left:791px;top:607px;width:315px;height:426px;border-radius:10px;background:linear-gradient(#f3f3f3,#fff 15%,#fff 85%,#f3f3f3)}
.testimonials h2{position:absolute;left:12px;top:12px;font-family:"PT Sans",sans-serif;font-weight:400;font-size:30px;color:var(--teal)}
.quote{position:absolute;left:8px;width:300px;font-family:"Noto Serif",serif;font-size:14px;line-height:20px;color:#777}
.quote p{width:177px;margin-left:20px;text-align:right}
.quote .photo{position:absolute;right:12px;top:0;width:88px;height:88px;border:2px solid #f0a820;background:linear-gradient(#b08060,#6a4a36)}
.quote .mark{position:absolute;font-family:"Noto Serif",serif;font-size:40px;color:#b8d13a;line-height:1}
.quote .who{position:absolute;left:10px;font-style:italic;font-size:13px;color:#333;line-height:20px}
.quote .who b{font-size:14px}
/* job board */
.board-title{position:absolute;left:460px;top:1224px;font-family:"PT Sans",sans-serif;font-weight:700;font-size:42px;color:var(--nav-green)}
.welcome{position:absolute;left:462px;top:1296px;display:flex;align-items:center;gap:12px;font-family:"PT Sans",sans-serif;font-size:30px;color:var(--brand-orange)}
.welcome span{font-size:26px;color:#e28a1a;font-family:"Arimo",sans-serif}
.mini-btn{position:absolute;height:30px;border-radius:5px;background:linear-gradient(#f8f8f8,#dcdcdc);box-shadow:0 1px 2px rgba(0,0,0,.3);display:flex;align-items:center;gap:8px;padding:0 12px;font-size:13px;color:#444}
.details{position:absolute;left:95px;top:1370px;width:1006px;height:187px;border-radius:10px;background:linear-gradient(#f1f1f1,#fff 40%,#f4f4f4)}
.details h2{position:absolute;left:24px;top:16px;font-family:"Noto Serif",serif;font-weight:400;font-size:26px;color:var(--nav-green)}
.detail{position:absolute;display:flex;align-items:center;gap:10px;font-size:14px;color:var(--text-green)}
.detail .dot{width:5px;height:5px;border-radius:50%;background:var(--text-green)}
.value{position:absolute;font-family:"Noto Serif",serif;font-size:19px;color:#444}
.tab{position:absolute;top:1598px;height:47px;border-radius:6px 6px 0 0;font-family:"PT Sans",sans-serif;font-size:21px;color:#fff;display:flex;align-items:center;justify-content:center;background:linear-gradient(#1e8a52,#136a3c)}
.tab.current{background:linear-gradient(#d88a1e,#c06a10);color:#fde2b0;top:1596px;height:49px}
.tab.add{background:linear-gradient(#5fae3a,#3f8a28);gap:10px}
.jobs-area{position:absolute;left:107px;top:1645px;width:986px;height:448px;background:linear-gradient(#7aa83a,#9fc03a);border-radius:0 0 6px 6px}
.jobs{position:absolute;left:124px;width:953px;border-collapse:collapse;background:#fff;font-size:12px;color:#333;border-radius:6px;overflow:hidden}
.jobs th{height:58px;background:var(--head-mint);color:#5bbd2a;font-size:13px;font-weight:700;line-height:21px;text-align:center}
.jobs td{height:39px;text-align:center}
.jobs tr.alt td.data{background:var(--row-grey)}
.jobs td.job{text-align:left;padding-left:18px;font-weight:700;color:#5bbd2a;line-height:26px}
.jobs td.job small{display:block;font-weight:400;font-size:11px;margin-left:24px;line-height:12px}
.acts{display:flex;gap:20px;justify-content:center;align-items:center;position:relative}
.badge{position:absolute;width:13px;height:13px;border-radius:50%;background:var(--red);color:#fff;font-size:8px;line-height:13px;text-align:center;right:8px;top:8px}
.tip{position:absolute;left:-8px;top:14px;background:#fdf3a8;border:1px solid #c8b85a;border-radius:4px;font-size:11px;color:#7a6a20;padding:1px 6px}
</style>
</head>
<body>
<svg width="0" height="0" style="position:absolute">
  <defs>
    <symbol id="tick" viewBox="0 0 16 16"><path d="M2 9l4 4 8-10" fill="none" stroke="#5bb52a" stroke-width="3" stroke-linecap="round"/></symbol>
    <symbol id="cross" viewBox="0 0 16 16"><path d="M3 3l10 10M13 3L3 13" stroke="#d0231c" stroke-width="3.5" stroke-linecap="round"/></symbol>
    <symbol id="mail" viewBox="0 0 26 18"><rect x="1" y="1" width="24" height="16" rx="1" fill="#f4f4f4" stroke="#c8c8c8"/><path d="M1 1l12 9 12-9" fill="none" stroke="#c8c8c8"/></symbol>
    <symbol id="chev" viewBox="0 0 30 50"><path d="M4 4l20 21L4 46" fill="none" stroke="#2f9a3c" stroke-width="10" stroke-linejoin="round"/></symbol>
  </defs>
</svg>

<!-- HOME PAGE -->
<main class="sheet" style="top:33px;height:1069px"></main>
<div class="logo-box" style="top:40px"><div class="logo-dot"></div><div class="logo-name">Voltaro<small>AUSTRALIA</small></div></div>
<nav class="main-nav"><span>HOME</span><span>HOW IT WORKS?</span><span>FAQ's</span><span>ABOUT US</span><span>TESTIMONIALS</span><span>CONTACT US</span></nav>
<a class="cta" style="left:459px">GET QUOTES</a>
<a class="cta" style="left:677px">ENERGY RATERS<small>Add your business</small></a>
<a class="cta" style="left:894px">ACTIVE<br>JOB BOARD</a>

<section class="process">
  <div class="step">Post a job</div><svg width="30" height="50"><use href="#chev"/></svg>
  <div class="step">Get as many quotes as you like</div><svg width="30" height="50"><use href="#chev"/></svg>
  <div class="step">Select energy quote that suits</div><svg width="30" height="50"><use href="#chev"/></svg>
  <div class="step">Approve payment</div><svg width="30" height="50"><use href="#chev"/></svg>
  <div class="step">Receive Rating</div>
</section>

<p class="intro">We provide you with solutions to your energy rating needs!&nbsp; Get up to 10 competitive quotes for your energy ratings from our database of professional accredited energy raters in all states and territories!</p>
<p class="lead">Voltaro australia is Australia's leading professional energy rating consultancy firm specializing in large scaled residential and commercial energy rating logistics.</p>
<div class="callout">It's Free, Fast and Easy to use and you get the best price and turnaround time that suits you!!<div class="big">Its a one stop shop for your energy rating needs!!</div></div>
<p class="register">Register with us, upload your job and specifications, and sit back and watch as energy raters provide quotes for your work!</p>
<ul class="benefits">
  <li><svg width="14" height="14"><use href="#tick"/></svg>Get up to 10 best priced quotes for your energy ratings</li>
  <li><svg width="14" height="14"><use href="#tick"/></svg>You save time</li>
  <li><svg width="14" height="14"><use href="#tick"/></svg>Be able to specify your desired turnaround times</li>
  <li><svg width="14" height="14"><use href="#tick"/></svg>You can upload a job for quoting anytime and anywhere</li>
  <li><svg width="14" height="14"><use href="#tick"/></svg>Choose a deadline for energy raters to supply quotes</li>
  <li><svg width="14" height="14"><use href="#tick"/></svg>Be able to track your numerous jobs in one place</li>
</ul>
<p class="free-note">Its totally free to be registered with us and there is no obligations or hidden catches!</p>

<form class="login">
  <label><span class="bullet"></span>User</label>
  <div class="field">miradel</div>
  <label><span class="bullet"></span>Password</label>
  <div class="field" style="color:#333;letter-spacing:2px">●●●●●●●●●●</div>
  <div class="forgot">Did you forget your password</div>
</form>

<aside class="testimonials">
  <h2>TESTIMONIALS</h2>
  <div class="quote" style="top:58px">
    <span class="mark" style="left:0;top:0">“</span>
    <p>Lorem ipsum dolor sit amet, consectetur adipiscing elit. Phasellus arcu magna, condimentum id consequat quis,</p>
    <div class="photo" role="img" aria-label="Portrait photo of a client"></div>
    <div class="who" style="top:134px"><b>Elena Marsh</b><br>Santo Domingo, Dominican Republic</div>
    <span class="mark" style="right:12px;top:140px">”</span>
  </div>
  <div class="quote" style="top:260px">
    <span class="mark" style="left:0;top:0">“</span>
    <p>Lorem ipsum dolor sit amet, consectetur adipiscing elit. Phasellus arcu</p>
    <div class="photo" role="img" aria-label="Portrait photo of a client" style="background:linear-gradient(#c9c9c9,#555)"></div>
    <div class="who" style="top:112px"><b>Tom Keller</b><br>Arizona, United States</div>
    <span class="mark" style="right:12px;top:116px">”</span>
  </div>
</aside>
<p class="copyright" style="top:1114px">Copyright 2010 - Voltaro Australia - All rights reserved</p>

<!-- JOB BOARD PAGE -->
<main class="sheet" style="top:1202px;height:937px"></main>
<div class="logo-box" style="top:1208px"><div class="logo-dot"></div><div class="logo-name">Voltaro<small>AUSTRALIA</small></div></div>
<h1 class="board-title">JOB BOARD</h1>
<div class="welcome"><span class="bullet" style="width:16px;height:16px"></span>Welcome, <span>Mira Delaine</span></div>
<a class="mini-btn" style="left:914px;top:1307px;width:101px"><svg width="24" height="14"><path d="M0 7l9-7v4h15v6H9v4z" fill="#d0231c"/></svg>Logout</a>
<a class="mini-btn" style="left:1031px;top:1307px;width:73px"><svg width="14" height="18"><text x="1" y="16" font-size="20" font-weight="700" fill="#1c5fb8" font-family="Arial">?</text></svg>Help</a>

<section class="details">
  <h2>Personal details</h2>
  <a class="mini-btn" style="left:877px;top:14px"><svg width="18" height="18"><path d="M3 15l2-6 8-8 4 4-8 8z" fill="#f0a820"/></svg>Edit profile</a>
  <div class="detail" style="left:48px;top:80px"><span class="dot"></span>Contact Name</div>
  <div class="detail" style="left:48px;top:113px"><span class="dot"></span>Company</div>
  <div class="detail" style="left:48px;top:146px"><span class="dot"></span>E-mail Address</div>
  <div class="value" style="left:199px;top:74px">Sam Porter</div>
  <div class="value" style="left:199px;top:109px">Voltaro Australia</div>
  <div class="value" style="left:199px;top:148px;font-family:Arimo,sans-serif;font-size:11px;color:var(--teal)">sporter@voltaro-australia.com</div>
  <div class="detail" style="left:514px;top:80px"><span class="dot"></span>Postal Address</div>
  <div class="value" style="left:665px;top:74px;line-height:33px">14 Alder Lane<br>BROOKVALE VIC 3999</div>
</section>

<div class="tab current" style="left:114px;width:160px">QUOTING JOBS</div>
<div class="tab" style="left:283px;width:140px">ACTIVE JOBS</div>
<div class="tab" style="left:433px;width:186px">COMPLETED JOBS</div>
<div class="tab add" style="left:873px;width:203px"><svg width="16" height="16"><path d="M6 0h4v6h6v4h-6v6H6v-6H0V6h6z" fill="#bfe68a"/></svg>ADD A NEW JOB</div>
<div class="jobs-area"></div>

<table class="jobs" style="top:1663px">
  <colgroup><col style="width:122px"><col style="width:107px"><col style="width:70px"><col style="width:104px"><col style="width:67px"><col style="width:66px"><col style="width:68px"><col style="width:104px"><col style="width:109px"><col style="width:136px"></colgroup>
  <tr><th>JOB</th><th>DEADLINE FOR<br>QUOTES</th><th>QUOTE<br>NUMBER</th><th>DATE RECEIVED</th><th>TOTAL<br>PRICE</th><th>REWORK<br>PRICE</th><th>TOTAL<br>PRICE</th><th>TURNAROUND<br>TIME</th><th>ACCREDITITION</th><th></th></tr>
  <tr class="alt"><td class="job" rowspan="3">+ Elm place<small>Edit job</small></td><td rowspan="3">April 20th</td><td class="data">111111</td><td class="data">April 15th</td><td class="data">$155,00</td><td class="data">$120,00</td><td class="data">$180,65</td><td class="data">1-5 days</td><td class="data">VIC</td><td class="data"><div class="acts"><svg width="16" height="16"><use href="#tick"/></svg><svg width="16" height="16"><use href="#cross"/></svg><svg width="26" height="18"><use href="#mail"/></svg><span class="tip">Accept</span></div></td></tr>
  <tr><td class="data">111156</td><td class="data">April 10th</td><td class="data">$250,00</td><td class="data">$150,00</td><td class="data">$265,00</td><td class="data">5-10 days</td><td class="data">QLD</td><td class="data"><div class="acts"><svg width="16" height="16"><use href="#tick"/></svg><svg width="16" height="16"><use href="#cross"/></svg><svg width="26" height="18"><use href="#mail"/></svg></div></td></tr>
  <tr class="alt"><td class="data">111186</td><td class="data">April 9th</td><td class="data">$125,00</td><td class="data">$100,00</td><td class="data">$129,65</td><td class="data">2 weeks</td><td class="data">SA</td><td class="data"><div class="acts"><svg width="16" height="16"><use href="#tick"/></svg><svg width="16" height="16"><use href="#cross"/></svg><svg width="26" height="18"><use href="#mail"/></svg><span class="badge">1</span></div></td></tr>
</table>

<table class="jobs" style="top:1861px">
  <colgroup><col style="width:122px"><col style="width:107px"><col style="width:70px"><col style="width:104px"><col style="width:67px"><col style="width:66px"><col style="width:68px"><col style="width:104px"><col style="width:109px"><col style="width:136px"></colgroup>
  <tr><th>JOB</th><th>DEADLINE FOR<br>QUOTES</th><th>QUOTE<br>NUMBER</th><th>DATE RECEIVED</th><th>TOTAL<br>PRICE</th><th>REWORK<br>PRICE</th><th>TOTAL<br>PRICE</th><th>TURNAROUND<br>TIME</th><th>ACCREDITITION</th><th></th></tr>
  <tr class="alt"><td class="job" rowspan="4">+ Elm place<small>Edit job</small></td><td rowspan="4">April 20th</td><td class="data">111111</td><td class="data">April 15th</td><td class="data">$155,00</td><td class="data">$120,00</td><td class="data">$180,65</td><td class="data">1-5 days</td><td class="data">VIC</td><td class="data"><div class="acts"><svg width="16" height="16"><use href="#tick"/></svg><svg width="16" height="16"><use href="#cross"/></svg><svg width="26" height="18"><use href="#mail"/></svg><span class="tip">Accept</span></div></td></tr>
  <tr><td class="data">111156</td><td class="data">April 10th</td><td class="data">$250,00</td><td class="data">$150,00</td><td class="data">$265,00</td><td class="data">5-10 days</td><td class="data">QLD</td><td class="data"><div class="acts"><svg width="16" height="16"><use href="#tick"/></svg><svg width="16" height="16"><use href="#cross"/></svg><svg width="26" height="18"><use href="#mail"/></svg></div></td></tr>
  <tr class="alt"><td class="data">111186</td><td class="data">April 9th</td><td class="data">$125,00</td><td class="data">$100,00</td><td class="data">$129,65</td><td class="data">2 weeks</td><td class="data">SA</td><td class="data"><div class="acts"><svg width="16" height="16"><use href="#tick"/></svg><svg width="16" height="16"><use href="#cross"/></svg><svg width="26" height="18"><use href="#mail"/></svg><span class="badge">1</span></div></td></tr>
  <tr><td class="data">111170</td><td class="data">April 9th</td><td class="data">$120,00</td><td class="data">$95,00</td><td class="data">$125,00</td><td class="data">2 weeks</td><td class="data">SA</td><td class="data"><div class="acts"><svg width="16" height="16"><use href="#tick"/></svg><svg width="16" height="16"><use href="#cross"/></svg><svg width="26" height="18"><use href="#mail"/></svg><span class="badge">10</span></div></td></tr>
</table>
<p class="copyright" style="top:2154px">Copyright 2010 - Voltaro Australia - All rights reserved</p>
</body>
</html>
```